Financial Sevices firm looking for Brochure design

Our company Veltmoor Capital and Holdings Limited (VeltHoldings)
i
Is an investment/advisory firm - www.veltholdings-grp.net
We invest in the energy sector in Africa and offer advisory services to Energy companies looking to invest in Africa. From oil and gas, to renewables (wind/solar). We are more focused on the "West African" Sub region
We need corporate brochure (Booklet style) to circulate to our corporate clients
We would like to see a design that considers the colours in our Logo (see website)
HI Guys, sorry been travelling. Seen some very good submissions and will be sending updates shortly
Reason: Dear Designers,
Thank you for participating in this project and for some of the great designs i've received so far. Unfortunately, due to the holidays, it has been difficult to consult with other members of my team. As a result, the project deadline is extended by about 12 days
I appreciate your understanding in the situation and looking forward to continuing the excellent collaboration in the coming days
Reason: Hi All,
Apologies for the multiple deadline extensions and thanks so much for all the designs which my team and I will be reviewing today and tomorrow.
We will be closing this project tomorrow by 6pm GMT (17th Jan 2014)
Thanks to all those that submitted such wonderful designs and goodluck!!
Project to be closed finally on 17th Jan 2014 at 6pm GMT
Banks, Investment Firms, Energy companies, Private Equity Funds
I have attached a Brochure that I created myself as an example of the type of information required but please also feel free to visit our website www.veltholdings-grp.net
Looking for any creative ideas you have to suplement the information provided.
Financial

```html
<!DOCTYPE html>
<html lang="en">
<head>
<meta charset="utf-8">
<title>VeltHoldings – Brochure Back Cover</title>
<link href="https://fonts.googleapis.com/css2?family=Montserrat:wght@500;700&display=swap" rel="stylesheet">
<style>
  :root {
    --backdrop: #eeeeee;
    --paper: #ffffff;
    --brand-red: #cc1426;
    --text-light: #ffffff;
  }
  html, body {
    margin: 0;
    padding: 0;
    width: 1200px;
    height: 849px;
    overflow: hidden;
    background: var(--backdrop);
  }
  .canvas {
    position: relative;
    width: 1200px;
    height: 849px;
  }
  .back-cover {
    position: absolute;
    left: 354px;
    top: 181px;
    width: 482px;
    height: 481px;
    background: var(--brand-red);
    font-family: "Montserrat", Arial, sans-serif;
  }
  .header-band {
    height: 92px;
    background: var(--paper);
    position: relative;
  }
  .wordmark {
    position: absolute;
    left: 41px;
    top: 40px;
    display: flex;
    align-items: center;
    gap: 4px;
    color: var(--brand-red);
    font-weight: 700;
    font-size: 13px;
    letter-spacing: 0.1px;
  }
  .wordmark-square {
    width: 10px;
    height: 10px;
    background: var(--brand-red);
  }
  .brand-mark {
    position: absolute;
    left: 41px;
    top: 288px;
    width: 20px;
    height: 20px;
    background: var(--text-light);
    border-radius: 2px;
  }
  .contact {
    position: absolute;
    left: 41px;
    top: 331px;
    color: var(--text-light);
    font-size: 8.3px;
    line-height: 11.5px;
    font-weight: 500;
  }
  .contact p { margin: 0 0 11.5px; }
  .contact .company { font-weight: 700; }
  .contact .label { font-weight: 700; }
</style>
</head>
<body>
<div class="canvas">
  <section class="back-cover">
    <header class="header-band">
      <div class="wordmark"><span class="wordmark-square"></span>veltholdings</div>
    </header>
    <div class="brand-mark" aria-hidden="true"></div>
    <address class="contact">
      <p class="company">VeltHoldings Limited</p>
      <p>14 Harrowgate Crescent<br>Off Calder Road<br>N.E. Quayside<br>Port Elland, Westmarch</p>
      <p><span class="label">E:.</span> info@veltholdings-grp.net<br><span class="label">W:.</span> www.veltholdings-grp.net</p>
    </address>
  </section>
</div>
</body>
</html>
```